Modern Billboard Ad for Criminal Defense Firm

10.5 x 36 We're looking for something to set us apart from the local competition. Looking for sleek and modern. We're a mid-sized firm in a small market city. We want to give the artist room to be creative on this one.
Thanks

Target Market(s)

Adult clients who have been charged with a crime/DWI

Industry/Entity Type

legal

Font styles to use
Serif
Sans Serif

Requirements
Must have
• Needs to have the firm name in large lettering. Law Offices of Marcus T Whitfield. “PLLC” does not have to be included. Phone number of (555) 384-1927 should be included but not the main focus.
Nice to have
• A call to action or something similar. “Don’t go it alone, call today.”, “ Arrested?”

```html
<!DOCTYPE html>
<html lang="en">
<head>
<meta charset="utf-8">
<title>Law Offices of Marcus T Whitfield — Billboard</title>
<link href="https://fonts.googleapis.com/css2?family=Alfa+Slab+One&family=PT+Sans:wght@700&display=swap" rel="stylesheet">
<style>
  :root {
    --page-bg: #e9ecef;
    --board-white: #f4f5f6;
    --band-blue: #1aa9e1;
    --band-blue-deep: #1590c4;
    --ink: #111213;
    --outline: #ffffff;
    --photo-light: #b9b9b9;
    --photo-dark: #4a4a4a;
  }
  * { margin: 0; padding: 0; box-sizing: border-box; }
  html, body {
    width: 1200px; height: 901px; overflow: hidden;
    background: var(--page-bg);
  }
  .billboard {
    position: absolute; left: 40px; top: 287px;
    width: 1120px; height: 327px;
    background: var(--board-white);
    overflow: hidden;
  }
  .blue-band {
    position: absolute; left: 0; right: 0; top: 40px; height: 260px;
    background: linear-gradient(90deg, var(--band-blue-deep), var(--band-blue) 45%, var(--band-blue-deep));
  }
  .attorney-portrait {
    position: absolute; left: 0; top: 8px; width: 250px; height: 292px;
    background: radial-gradient(ellipse at 55% 30%, var(--photo-light), var(--photo-dark) 80%);
  }
  .firm-name {
    position: absolute; left: 270px; top: 62px; width: 830px;
    font-family: "Alfa Slab One", serif;
    font-size: 60px; line-height: 70px;
    color: var(--ink);
    text-transform: uppercase;
    -webkit-text-stroke: 6px var(--outline);
    paint-order: stroke fill;
    letter-spacing: 0.5px;
  }
  .firm-name span { display: block; white-space: nowrap; }
  .call-line {
    position: absolute; left: 270px; top: 240px;
    font-family: "PT Sans", sans-serif; font-weight: 700;
    font-size: 21px; color: var(--ink);
    white-space: nowrap;
  }
  .call-line .phone { margin-left: 28px; }
</style>
</head>
<body>
  <div class="billboard">
    <div class="blue-band"></div>
    <div class="attorney-portrait" role="img" aria-label="Black and white portrait of the attorney in a vest and tie, jacket over shoulder"></div>
    <h1 class="firm-name">
      <span>Law Offices of</span>
      <span>Marcus T Whitfield</span>
    </h1>
    <p class="call-line">“Don’t go it alone, call today. Arrested?”<span class="phone">(555) 384-1927</span></p>
  </div>
</body>
</html>
```